Brochure for Dog Daycare/Overnight Facility

Looking for a multi page brochure for my dog daycare, overnight care, and grooming facility.

Content to be taken from our current website. Please note our website will be updated so please don't take any design elements from it.

Brochure should be professional yet personable with stock images of dogs playing and having fun.

Please see the attached file with the business card so you can see the blue and green colors that we use to brand ourselves.

Here are the different sections to include for content which can all be found on our website at: www.PawHavenLodge.com

Highlight our three main services: Go to the services tab and pull the content from Daycare, Overnight Care, and Grooming.

Use testimonials throughout found: About us tab, left side of page under 'what our clients say'.

Facility highlights: About us tab, left side under 'Facility'.

What makes us different: About us tab, left side of page.

Include the following Frequently Asked Questions and answers:
What is dog daycare?
How often do dog owners take their dogs to Daycare?
I have an old dog, will he/she enjoy this environment?
Does my dog have to be spayed or neutered?
Do you offer indoor and outdoor play areas?
Can I take a tour?
What qualifications do staff members have?
What sets you apart from your competitors?

Make sure to include: phone number, web address, e-mail address, mailing address.
Updates

Thank you all for your submissions.  We are having a hard time deciding with this project.  Hope to have made a decision in the next day or so.

Target Market(s)

Dog owners would love their pets. Medium to higher income. Ages 25-60.

Industry/Entity Type

Business

Requirements
Must have
• Must have all of the content pulled from our website.

Photos of dogs and dogs playing.

Our contact information.

Nice to have
• I would like a corresponding price sheet that is not part of the brochure but can be slid inside. Our pricing can be found on our website. I can get into more specifics on pricing if you choose to provide this option.
Should not have
• Anything cat related.

Should not be cutesie, must be professional and personable. Displaying trust.

```html
<!DOCTYPE html>
<html lang="en">
<head>
<meta charset="utf-8">
<title>Paw Haven Lodge – Tri-fold Brochure</title>
<link rel="stylesheet" href="https://fonts.googleapis.com/css2?family=Arimo:wght@400&family=Fira+Sans+Condensed:wght@400;500&display=swap">
<style>
  :root {
    --brand-green: #a9c43a;
    --brand-blue: #a4dbe4;
    --brand-brown: #4b4036;
    --ink: #2b2b2b;
    --panel-white: #ffffff;
    --panel-grey: #e4e4e4;
    --page-bg: #ffffff;
  }
  * { margin: 0; padding: 0; box-sizing: border-box; }
  html, body { width: 1200px; height: 927px; overflow: hidden; background: var(--page-bg); }
  .brochure { position: relative; width: 1200px; height: 927px; display: flex; }
  .panel { position: relative; height: 927px; overflow: hidden; }

  /* Grooming panel */
  .panel--grooming {
    width: 400px;
    background: linear-gradient(90deg, var(--panel-white) 0%, var(--panel-white) 60%, var(--panel-grey) 100%);
  }
  .section-title {
    font-family: "Fira Sans Condensed", sans-serif;
    font-weight: 500;
    font-size: 23px;
    text-align: center;
  }
  .panel--grooming .section-title { color: var(--brand-green); margin: 62px 0 14px 0; padding-left: 0; }
  .grooming-copy {
    font-family: Arimo, sans-serif;
    font-size: 14.2px;
    line-height: 18.5px;
    color: var(--ink);
    padding: 0 36px 0 28px;
  }
  .grooming-copy p { margin-bottom: 13px; }
  .grooming-photo {
    position: absolute; left: 0; top: 400px; width: 400px; height: 527px;
    background:
      radial-gradient(ellipse 120px 150px at 235px 150px, #5a5550 0%, #8a8682 60%, rgba(255,255,255,0) 100%),
      linear-gradient(180deg, rgba(255,255,255,0) 0%, rgba(255,255,255,0) 40%, #86c7cf 60%, #79bcc6 100%);
  }

  /* Hours panel */
  .panel--hours {
    width: 398px;
    background: var(--brand-green);
    text-align: center;
    font-family: Arimo, sans-serif;
    color: var(--brand-brown);
  }
  .panel--hours .section-title { color: #fff; margin-top: 58px; margin-bottom: 2px; }
  .hours-list { font-size: 17.5px; line-height: 27px; }
  .hours-block { margin-bottom: 27px; }
  .brand-lockup { margin-top: 30px; }
  .brand-mark { display: block; width: 64px; height: 64px; background: var(--brand-blue); margin: 0 auto 16px; }
  .brand-name {
    font-family: "Fira Sans Condensed", sans-serif;
    font-weight: 400;
    font-size: 34px;
    letter-spacing: 2px;
    color: var(--brand-brown);
    line-height: 1;
  }
  .brand-tagline {
    font-family: "Fira Sans Condensed", sans-serif;
    font-size: 22px;
    color: var(--brand-brown);
    margin-top: 14px;
  }
  .contact { font-size: 17px; line-height: 21.5px; margin-top: 16px; font-style: normal; }

  /* Cover panel */
  .panel--cover {
    width: 402px;
    background:
      radial-gradient(ellipse 190px 260px at 190px 560px, #8f8b86 0%, #6c6964 55%, #4e4c49 100%),
      #55524f;
  }
  .cover-photo { position: absolute; inset: 0; }
  .cover-brand { position: absolute; top: 38px; left: 0; width: 100%; text-align: center; }
  .cover-brand .brand-mark { width: 70px; height: 70px; margin-bottom: 14px; }
  .cover-brand .brand-name { color: #f1f1f1; font-size: 33px; }
  .cover-tagline {
    position: absolute; right: 24px; top: 668px; text-align: right;
    font-family: "Fira Sans Condensed", sans-serif;
    color: var(--brand-blue);
    font-size: 34px; line-height: 36px;
  }
  .cover-tagline .emph {
    display: block; color: var(--brand-green);
    font-size: 58px; line-height: 56px; letter-spacing: 11px; margin-right: -8px;
  }
</style>
</head>
<body>
<main class="brochure">
  <section class="panel panel--grooming">
    <h2 class="section-title">Grooming</h2>
    <div class="grooming-copy">
      <p>Every dog deserves the best and our professional dog groomers are ready to cater to their every need. Our high quality, full service grooming includes a bath with your choice of shampoo (we use all natural products), nail trim, ear cleaning, brush out and haircut if necessary.</p>
      <p>Every grooming treatment or service is available a la carte and can be done on their own or as a complement to any other grooming service. Prices vary by breed, size or coat condition and are by appointment only. Please call today to schedule your appointment or to ask about any of our fabulous spa services.</p>
      <p>Proof of rabies vaccination and a completed application packet is required prior to any grooming service.</p>
    </div>
    <div class="grooming-photo" role="img" aria-label="Photo of a small black and white long-eared dog holding a light blue towel in its mouth"></div>
  </section>

  <section class="panel panel--hours">
    <h2 class="section-title">Hours</h2>
    <div class="hours-list">
      <div class="hours-block">M-F 6am – 6pm<br>Sat. 8am – 6pm<br>Sun 10 am – 6pm</div>
      <div class="hours-block">Closed – Easter, July 4th, Thanksgiving,<br>Christmas Day</div>
      <div class="hours-block">We are open for Overnight pick up and<br>drop-off only:<br>Memorial Day - 3PM-5PM<br>Labor Day - 3PM-5PM<br>Christmas Eve Day - 6AM-12PM<br>New Year’s Eve Day - 6AM-12PM<br>New Year’s Day - 10AM-2PM</div>
    </div>
    <div class="brand-lockup">
      <span class="brand-mark"></span>
      <div class="brand-name">PAW HAVEN LODGE</div>
      <div class="brand-tagline">The Next Best Thing to Being Home</div>
      <address class="contact">2450 Meadowbrook Lane<br>Fairview, WI 54100<br>P: 920 555 0142<br>F: 920 555 0148<br>info@pawhavenlodge.com</address>
    </div>
  </section>

  <section class="panel panel--cover">
    <div class="cover-photo" role="img" aria-label="Black and white close-up photo of a large fluffy dog looking at the camera"></div>
    <div class="cover-brand">
      <span class="brand-mark"></span>
      <div class="brand-name">PAW HAVEN LODGE</div>
    </div>
    <div class="cover-tagline">the next best<br>best thing to<span class="emph">being</span><span class="emph">home</span></div>
  </section>
</main>
</body>
</html>
```